On-the-go, individually packaged flushable wipe packaging

Design the front and back of an individually packaged flushable wipe product.

The package is 4 inches tall and 2 inches wide. There are only two sides to the package, front and back. It is constructed of two sheets of printed, foil-lined plastic that are heat welded together.

The front should be decorative and playful and have space for a logo / product name on it (no logo has been created yet so use your imagination if you wish). It should be unisex and envoke somewhat outdoorsy vibes that would appeal to mountain bikers, marathon runners, travelers, and adventurers of all kinds. It can draw attention to itself through color but not through potty humor or bathroom references. People should be able to take these to work or send them with their children to school with being embarrassed.

Important note: Similar to business cards, the packaging material is printed and then cut in a grid. The machine that cuts the packaging may be off by a couple millimeters so any artwork or colors that extend to the sides of the packaging should continue onto the opposite side of the next package like a tesselation or book-matched wood, left side should match up to right side and top should match up to bottom.

The back should contain the follow information (iconography and layout up to you):

- Contains one hygienic towelette
- (Key selling points)
- Flushable & Biodegradable
- 100% natural fibers
- Gentle cleansing formula
- No parabens or fragrances
- (For use on…)
- Hands
- Face*
- Body
- Nether areas
- Messy surfaces
- *Avoid eyes/forehead before sweating and scruff (snags fibers)
- Please care for our planet, cities, and sewer systems by recycling this packaging after use. Do not flush packaging.

```html
<!DOCTYPE html>
<html lang="en">
<head>
<meta charset="utf-8">
<title>Roamwell Flushable Wet Wipe – Packet Front and Back</title>
<link href="https://fonts.googleapis.com/css2?family=Bebas+Neue&family=Lexend:wght@400;600;700;800&display=swap" rel="stylesheet">
<style>
  :root {
    --teal: #4bbbba;
    --teal-light: #7ccfcb;
    --navy: #0b4f9e;
    --white: #ffffff;
    --grey: #8a8f94;
    --page: #ffffff;
  }
  * { box-sizing: border-box; margin: 0; padding: 0; }
  html, body { width: 1200px; height: 952px; overflow: hidden; background: var(--page); }
  body { position: relative; font-family: "Lexend", sans-serif; }

  .packet { position: absolute; background: var(--teal); overflow: hidden; }
  .packet--front { left: 182px; top: 78px; width: 404px; height: 803px; }
  .packet--back  { left: 649px; top: 80px; width: 401px; height: 802px; }

  .seal-field { position: absolute; left: 30px; top: 36px; width: 343px; height: 730px;
    background: linear-gradient(180deg, var(--teal-light) 0%, var(--teal) 50%); }
  .packet--back .seal-field { left: 27px; top: 34px; width: 342px; }

  /* front */
  .front-wave { position: absolute; left: 0; top: 395px; width: 404px; height: 408px; }
  .brand-flag { position: absolute; left: 76px; top: 124px; width: 251px; height: 200px; }
  .brand-name { position: absolute; left: 76px; top: 144px; width: 251px; text-align: center;
    font-weight: 800; font-size: 60px; line-height: 64px; color: var(--navy); letter-spacing: -1px; }
  .product-name { position: absolute; left: 76px; top: 336px; width: 251px; text-align: center;
    font-family: "Bebas Neue", sans-serif; font-size: 31px; line-height: 31px; letter-spacing: 2px; color: var(--white); }

  .benefit { position: absolute; left: 82px; display: flex; align-items: center; }
  .benefit__icon { width: 75px; height: 54px; border-radius: 12px;
    background: linear-gradient(135deg, #bfe6e3, #8fd3ce); flex: none; }
  .benefit__text { margin-left: 10px; font-weight: 700; font-size: 17px; line-height: 19px;
    color: var(--navy); letter-spacing: 0.5px; }
  .benefit--formula { top: 443px; }
  .benefit--fibers  { top: 513px; }
  .benefit--free    { top: 592px; }

  .variant-pill { position: absolute; left: 115px; top: 682px; width: 173px; height: 29px;
    border: 2px solid var(--navy); border-radius: 15px; text-align: center;
    font-size: 15px; line-height: 25px; letter-spacing: 3.5px; color: var(--navy); }
  .net-contents { position: absolute; left: 0; top: 728px; width: 404px; text-align: center;
    font-size: 10.5px; line-height: 13px; letter-spacing: 1.5px; color: var(--grey); }

  /* back */
  .use-box { position: absolute; left: 55px; top: 144px; width: 291px; height: 228px;
    border: 1.5px solid rgba(255,255,255,0.75); border-radius: 8px; color: var(--white); }
  .use-box__title { position: absolute; top: 22px; width: 100%; text-align: center;
    font-weight: 700; font-size: 20px; line-height: 24px; letter-spacing: 0.5px; }
  .use-list { position: absolute; list-style: none; font-weight: 700; font-size: 20px; line-height: 20px; }
  .use-list li { position: relative; padding-left: 24px; }
  .use-list li svg { position: absolute; left: 0; top: 1px; }
  .use-list--a { left: 21px; top: 63px; }
  .use-list--a li { margin-bottom: 13px; }
  .use-list--b { left: 138px; top: 63px; }
  .use-list--b li { margin-bottom: 8px; }
  .use-box__note { position: absolute; left: 21px; top: 170px; font-size: 14px; line-height: 17px; }

  .claim { position: absolute; left: 74px; top: 407px; width: 268px; height: 79px;
    border: 1.5px solid rgba(255,255,255,0.75); border-radius: 10px; border-left: none; }
  .claim__pct { position: absolute; left: 70px; top: 402px; font-family: "Bebas Neue", sans-serif;
    font-size: 56px; line-height: 56px; letter-spacing: 1px; color: var(--navy); }
  .claim__line { position: absolute; font-family: "Bebas Neue", sans-serif; color: var(--white);
    font-size: 37px; line-height: 37px; }
  .claim__line--1 { left: 182px; top: 415px; letter-spacing: 1.5px; }
  .claim__line--2 { left: 78px; top: 446px; letter-spacing: 2.5px; }

  .back-copy { position: absolute; left: 65px; width: 300px; color: var(--white);
    font-size: 16.5px; line-height: 20.5px; }
  .back-copy--directions { top: 513px; }
  .back-copy--planet { top: 571px; }
</style>
</head>
<body>

<section class="packet packet--front" aria-label="Packet front">
  <div class="seal-field"></div>
  <svg class="front-wave" viewBox="0 0 404 408" aria-hidden="true">
    <path d="M0 18 C70 -10 150 -2 230 12 C300 25 350 28 404 10 L404 408 L0 408 Z" fill="var(--white)"/>
    <rect x="0" y="371" width="404" height="37" fill="var(--teal)"/>
  </svg>
  <svg class="brand-flag" viewBox="0 0 251 200" aria-hidden="true">
    <path d="M0 0 H251 V191 C200 205 150 196 95 183 C55 175 25 178 0 185 Z" fill="var(--white)"/>
  </svg>
  <div class="brand-name">ROAM<br>WELL</div>
  <div class="product-name">FLUSHABLE WET WIPE</div>

  <div class="benefit benefit--formula">
    <div class="benefit__icon" role="img" aria-label="Water drop icon"></div>
    <div class="benefit__text">GENTLE<br>CLEANSING<br>FORMULA</div>
  </div>
  <div class="benefit benefit--fibers">
    <div class="benefit__icon" role="img" aria-label="Leaf sprout icon"></div>
    <div class="benefit__text">100% NATURAL<br>FIBERS</div>
  </div>
  <div class="benefit benefit--free">
    <div class="benefit__icon" role="img" aria-label="Hand holding a leaf icon"></div>
    <div class="benefit__text">NO PARABENS<br>OR FRAGRANCES</div>
  </div>

  <div class="variant-pill">UNSCENTED</div>
  <div class="net-contents">1 FLUSHABLE WET WIPE<br>8"X6" (20.32X15.24CM]</div>
</section>

<section class="packet packet--back" aria-label="Packet back">
  <div class="seal-field"></div>

  <div class="use-box">
    <div class="use-box__title">FOR USE ON:</div>
    <ul class="use-list use-list--a">
      <li><svg width="16" height="16" viewBox="0 0 16 16"><rect x="1" y="3" width="12" height="12" fill="none" stroke="#fff" stroke-width="1.6"/><path d="M4 8 L7 12 L14 1" fill="none" stroke="var(--navy)" stroke-width="2.2"/></svg>HANDS</li>
      <li><svg width="16" height="16" viewBox="0 0 16 16"><rect x="1" y="3" width="12" height="12" fill="none" stroke="#fff" stroke-width="1.6"/><path d="M4 8 L7 12 L14 1" fill="none" stroke="var(--navy)" stroke-width="2.2"/></svg>FACE*</li>
      <li><svg width="16" height="16" viewBox="0 0 16 16"><rect x="1" y="3" width="12" height="12" fill="none" stroke="#fff" stroke-width="1.6"/><path d="M4 8 L7 12 L14 1" fill="none" stroke="var(--navy)" stroke-width="2.2"/></svg>BODY</li>
    </ul>
    <ul class="use-list use-list--b">
      <li><svg width="16" height="16" viewBox="0 0 16 16"><rect x="1" y="3" width="12" height="12" fill="none" stroke="#fff" stroke-width="1.6"/><path d="M4 8 L7 12 L14 1" fill="none" stroke="var(--navy)" stroke-width="2.2"/></svg>NETHER<br>AREAS</li>
      <li><svg width="16" height="16" viewBox="0 0 16 16"><rect x="1" y="3" width="12" height="12" fill="none" stroke="#fff" stroke-width="1.6"/><path d="M4 8 L7 12 L14 1" fill="none" stroke="var(--navy)" stroke-width="2.2"/></svg>MESSY<br>SURFACES</li>
    </ul>
    <p class="use-box__note">*Avoid eyes/forehead before<br>sweating and scruff (snags fibers)</p>
  </div>

  <div class="claim"></div>
  <div class="claim__pct">100%</div>
  <div class="claim__line claim__line--1">FLUSHABLE</div>
  <div class="claim__line claim__line--2">&amp; BIODEGRADABLE</div>

  <p class="back-copy back-copy--directions">DIRECTIONS: Tear open, unfold<br>wipe, use and flush.</p>
  <p class="back-copy back-copy--planet">Please care for our planet, cities,<br>and sewer systems by recycling<br>this packaging after use. Do not<br>flush packaging.</p>
</section>

</body>
</html>
```